Lanterns Over Saltmere - Islamic Book about death, grave and the hereafter

We need a complete redesign of an old book cover. It is a book about death, the grave, the day of judgment, hellfire and paradise. i've attached our old bookcover. you can take new colors and change completly the design. It is up to you!

```html
<!DOCTYPE html>
<html lang="de">
<head>
<meta charset="utf-8">
<title>Lanterns Over Saltmere – Buchumschlag</title>
<link href="https://fonts.googleapis.com/css2?family=Tinos:wght@400;700&family=Archivo+Narrow:wght@400;500&display=swap" rel="stylesheet">
<style>
  :root {
    --stage: #000000;
    --sky-blue: #3f7ed0;
    --sky-pale: #cfe3ef;
    --mist: #eef3dc;
    --meadow: #a9c25a;
    --meadow-deep: #6f8f2c;
    --bloom: #f2d51c;
    --gold-light: #ffe07a;
    --gold: #f2b531;
    --gold-deep: #b8741a;
    --bronze: #6b3a0c;
    --ink-brown: #3d1e05;
  }
  * { box-sizing: border-box; margin: 0; padding: 0; }
  html, body { width: 1200px; height: 818px; overflow: hidden; background: var(--stage); }
  .canvas { position: relative; width: 1200px; height: 818px; background: var(--stage); }

  .back-cover {
    position: absolute; left: 80px; top: 50px; width: 485px; height: 714px;
    background:
      radial-gradient(ellipse 60% 35% at 40% 48%, rgba(255,252,230,.95), rgba(255,252,230,0) 70%),
      linear-gradient(180deg, var(--sky-blue) 0%, #6fa1da 18%, var(--sky-pale) 38%, var(--mist) 52%, #c9d98a 70%, var(--meadow) 84%, var(--meadow-deep) 100%);
  }

  .spine {
    position: absolute; left: 565px; top: 50px; width: 80px; height: 714px;
    background: linear-gradient(180deg, var(--gold) 0%, #f4b93a 30%, var(--gold-deep) 62%, var(--bronze) 85%, var(--ink-brown) 100%);
  }
  .spine-title {
    position: absolute; left: 40px; top: 272px;
    transform: translate(-50%, -50%) rotate(-90deg);
    white-space: nowrap;
    font-family: "Tinos", serif; font-size: 36px; color: var(--ink-brown);
  }
  .spine-publisher {
    position: absolute; left: 13px; top: 540px; width: 54px; height: 84px;
    background: linear-gradient(180deg, #e9b96a, #c98a3a);
    border: 1px solid #8a5a1e;
    display: flex; flex-direction: column; align-items: center; justify-content: center; gap: 6px;
    font-family: "Tinos", serif; font-size: 8px; font-weight: 700; color: var(--ink-brown);
    text-align: center; line-height: 1.1;
  }
  .spine-publisher .mark { width: 14px; height: 14px; background: var(--ink-brown); }

  .front-cover {
    position: absolute; left: 645px; top: 50px; width: 483px; height: 714px; overflow: hidden;
  }
  .front-photo {
    position: absolute; inset: 0;
    background:
      radial-gradient(ellipse 22% 30% at 55% 45%, rgba(245,240,230,.9), rgba(245,240,230,0) 75%),
      radial-gradient(ellipse 40% 25% at 30% 20%, rgba(255,255,255,.85), rgba(255,255,255,0) 70%),
      linear-gradient(180deg, #6d9ed8 0%, var(--sky-pale) 22%, var(--mist) 45%, #c6d98a 65%, var(--meadow) 82%, var(--meadow-deep) 100%);
  }
  .author {
    position: absolute; top: 48px; left: 0; width: 100%; padding-left: 20px; text-align: center;
    font-family: "Tinos", serif; font-weight: 700; font-size: 25px; letter-spacing: .3px;
    color: var(--gold-deep); text-shadow: 0 1px 0 #ffe9a8, 0 2px 3px rgba(80,40,0,.35);
  }
  .title { position: absolute; left: 0; width: 100%; font-family: "Tinos", serif; }
  .title-line {
    display: block; text-align: center;
    background: linear-gradient(180deg, var(--gold-light) 0%, var(--gold) 45%, var(--gold-deep) 60%, var(--bronze) 100%);
    -webkit-background-clip: text; background-clip: text; color: transparent;
    filter: drop-shadow(0 2px 2px rgba(40,20,0,.55));
  }
  .title-small { position: absolute; top: 410px; left: 40px; width: 443px; font-size: 50px; }
  .title-large { position: absolute; top: 462px; left: 10px; width: 473px; font-size: 74px; letter-spacing: -1px; }
  .subtitle-band {
    position: absolute; left: 0; top: 566px; width: 483px; height: 32px;
    background: linear-gradient(90deg, var(--bronze) 0%, var(--gold-deep) 25%, var(--gold) 60%, var(--gold-light) 100%);
    display: flex; align-items: center; justify-content: center;
    font-family: "Archivo Narrow", sans-serif; font-size: 26px; color: var(--ink-brown);
  }
  .publisher {
    position: absolute; top: 654px; left: 0; width: 100%; padding-left: 130px; text-align: center;
    font-family: "Tinos", serif; font-weight: 700; font-size: 17px; color: var(--bronze);
  }
</style>
</head>
<body>
<main class="canvas">
  <section class="back-cover" role="img" aria-label="Misty blue sky with clouds over a field of yellow wildflowers"></section>

  <section class="spine">
    <div class="spine-title">Lanterns Over SALTMERE</div>
    <div class="spine-publisher"><span class="mark"></span>Lantern House Press</div>
  </section>

  <section class="front-cover">
    <div class="front-photo" role="img" aria-label="Woman in a white dress with hands clasped, eyes closed, in a sunlit field of yellow flowers under a cloudy sky"></div>
    <p class="author">MIRA HALDEN-SURE</p>
    <h1 class="title">
      <span class="title-line title-small">Lanterns Over</span>
      <span class="title-line title-large">SALTMERE</span>
    </h1>
    <p class="subtitle-band">Über den tod und das leben danach</p>
    <p class="publisher">Lantern House Press</p>
  </section>
</main>
</body>
</html>
```